依頼詳細
当社のリーフレットやウェブサイトやその他資料に基づいたデザインでお願い致します。
記載項目
榊原会館 月照苑 有限会社みのり堂
https://gessho-en.example/
サイズ
A4
ページ数
4ページ
希望イメージ
シンプル 複雑
単色 カラフル
暗い 明るい
日常 高級
遊び心 厳粛
未来的 伝統的
女性的 男性的
希望する色
青系、水色系、無彩色系
納品ファイル
補足説明
■ 選んだ理由

この度の提案では従業員一同ぼんやりとイメージがありそれに一番近かった、またごちゃごちゃしていないデザイン、お花のチョイスなども決め手でした。

■ 提案者全員のお礼・コメント

はじめての依頼になりましたが、少量のページ数ながらみなさんのご提案はすばらしかったです。
資料を具体的にわかりやすくご提案いただいたのに採用できないことは非常に残念に感じます。
この度は誠にありがとうございました。

```html
<!DOCTYPE html>
<html lang="ja">
<head>
<meta charset="utf-8">
<title>榊原会館 月照苑</title>
<link rel="stylesheet" href="https://fonts.googleapis.com/css2?family=Yuji+Boku&family=Zen+Kaku+Gothic+New:wght@500&display=swap">
<style>
  :root {
    --paper: #ffffff;
    --ink-navy: #1b3150;
    --ink-text: #2a2f36;
    --cloud-tone: #e4e9ee;
    --wave-top: rgba(205, 217, 228, 0);
    --wave-mid: #dfe6ed;
    --wave-deep: #d3dde7;
    --moon-core: rgba(125, 146, 168, 0.55);
    --moon-edge: rgba(190, 204, 218, 0);
    --trim: #9a9a9a;
  }
  html, body {
    margin: 0;
    padding: 0;
    overflow: hidden;
    background: var(--paper);
  }
  .cover {
    position: relative;
    width: 875px;
    height: 1200px;
    overflow: hidden;
    background: var(--paper);
  }
  .wave-field {
    position: absolute;
    left: 44px;
    right: 44px;
    top: 470px;
    bottom: 52px;
    background: linear-gradient(to bottom, var(--wave-top) 0%, var(--wave-mid) 35%, var(--wave-deep) 100%);
  }
  .cloud-band {
    position: absolute;
    background: linear-gradient(to right, var(--cloud-tone), rgba(228, 233, 238, 0.6));
  }
  .cloud-band--upper-left { left: 80px; top: 80px; width: 250px; height: 130px; border-radius: 40px; }
  .cloud-band--right { left: 700px; top: 285px; width: 140px; height: 125px; border-radius: 40px 0 0 40px; }
  .moon-area {
    position: absolute;
    left: 140px;
    top: 390px;
    width: 570px;
    height: 650px;
    border-radius: 50%;
    background: radial-gradient(ellipse at 55% 62%, var(--moon-core) 0%, rgba(160, 178, 196, 0.3) 45%, var(--moon-edge) 72%);
  }
  .venue-name {
    position: absolute;
    left: 596px;
    top: 100px;
    margin: 0;
    writing-mode: vertical-rl;
    font-family: "Zen Kaku Gothic New", sans-serif;
    font-weight: 500;
    font-size: 64px;
    line-height: 1;
    letter-spacing: 12px;
    color: var(--ink-text);
  }
  .hall-title {
    position: absolute;
    left: 325px;
    top: 225px;
    margin: 0;
    writing-mode: vertical-rl;
    font-family: "Yuji Boku", serif;
    font-weight: 400;
    font-size: 225px;
    line-height: 1;
    letter-spacing: 48px;
    color: var(--ink-navy);
  }
  .trim-marks {
    position: absolute;
    left: 0;
    top: 0;
  }
</style>
</head>
<body>
<main class="cover">
  <div class="wave-field" role="img" aria-label="青海波の波模様"></div>
  <div class="cloud-band cloud-band--upper-left" role="img" aria-label="雲の文様"></div>
  <div class="cloud-band cloud-band--right" role="img" aria-label="雲の文様"></div>
  <div class="moon-area" role="img" aria-label="三日月のイラスト"></div>

  <h2 class="venue-name">榊原会館</h2>
  <h1 class="hall-title">月照苑</h1>

  <svg class="trim-marks" width="875" height="1200" viewBox="0 0 875 1200" aria-hidden="true" stroke="var(--trim)" stroke-width="1" fill="none">
    <path d="M44 0V40M0 52H34M831 0V40M875 52H841M44 1200V1160M0 1148H34M831 1200V1160M875 1148H841"/>
    <path d="M437 0V30M417 18H457M437 1200V1170M417 1182H457M0 600H30M18 580V620M875 600H845M857 580V620"/>
  </svg>
</main>
</body>
</html>
```